Lindwerk - We create living space - needs a web/WIX design

The website will be in the German language.
During the contest, I welcome designs with English text.
I will provide the German text to the winner.
We prefer WIX-Design for the future, if possible to make the website WiX-ready;

The text to be used in the webpage:
In the project description I’ve written a text about our company in English and in German – as you asked for. Please use this text in the first step.

QUALITY, EXPERTISE and EXPERIENCE
EVERYTHING UNDER A SINGLE ROOF

We are a real estate company based in Vienna, Austria. Our company's main competences are planning, conception, development, erection, sale/renting and management of properties. "We make best quality for the best price" - with this motto LINDWERK offers living space in high quality in Austria as well as in other countries. Thereby the working area of our property development focusses on both new construction and attic extensions.

QUALITÄT, KOMPETENZ UND ERFAHRUNG
ALLES UNTER EINEM DACH​

LINDWERK ist ein Komplettanbieter für Wohnimmobilien von der Vision, Konzeption, Entwicklung, Planung, Errichtung und Verkauf/Vermietung bis zur Hausverwaltung. „Wir bauen beste Qualität zum besten Preis“, unter diesem Motto bietet LINDWERK qualitativ hochwertigen, lebenswerten und nachhaltig gebauten Wohnraum sowohl in Österreich als auch in anderen Ländern an. Dabei konzentriert sich das Arbeitsfeld unserer Bauträgergesellschaft auf die beiden Kernbereiche Neubau und Dachgeschossausbau.

In the boxes “Must haves”, “Nice to haves”, “Should not haves” I’ve mentioned everything the designers need to know (font, colours etc.). AS I’ve received already some very good designs, there should be everything clear for the designers.

During the contest: homepage is welcome

Target Market(s)

Austria, Germany, Europe, Israel, USA; we would like to reach families, singles, male, female, general population and also investors

Industry/Entity Type

Real Estate Development

Number of Pages Required

5+ page

Font styles to use
Other font styles liked:
• See Upload

Colors

Designer to choose colors to be used in the design.

Requirements
Must have
• Pages called: "Company", "Projects", "Investments", "Partner", "Contact"; Link to projects; subsides (Team, News); enough space for renderings; Our company colours are yellow, grey, white and black (see our logo) - our website should be designed in this colours; Website in friendly and light colours
Nice to have
• Our company font for titles - attached; Eventually other font for the text - better readable; We prefer WIX-Design for the future, if possible to make the website WiX-ready.
• It should be clear, that the font in the attachement should be used; the provided files are pictures of our interior designs and the logo; we expect creativity from the designers, so they should use the best pictures in their opinion.
Should not have
• dark design

```html
<!DOCTYPE html>
<html lang="en">
<head>
<meta charset="utf-8">
<title>Lindwerk – We create living space</title>
<link rel="stylesheet" href="https://fonts.googleapis.com/css2?family=Exo+2:wght@300;400;500&family=Lato:wght@400;700&display=swap">
<style>
:root{
  --yellow:#ffe600;
  --yellow-deep:#f2cf00;
  --ink:#222;
  --text:#555;
  --muted:#777;
  --grey-band:#ececec;
  --grey-card:#f2f2f2;
  --nav:#2a2a2a;
  --footer:#5a5a5a;
  --white:#fff;
}
*{box-sizing:border-box;margin:0;padding:0}
html,body{width:1200px;height:3636px;overflow:hidden;background:var(--white)}
body{position:relative;font-family:"Lato",Arial,sans-serif;color:var(--text)}
.abs{position:absolute}
section,header,nav,footer{position:absolute;left:0;width:1200px}
.title{position:absolute;left:0;width:1200px;text-align:center;font-family:"Exo 2",sans-serif;font-weight:300;font-size:40px;letter-spacing:3px;color:#4d4d4d}
p{font-size:14px;line-height:24px}

/* header */
.site-header{top:0;height:104px}
.brand{left:78px;top:32px;display:flex;align-items:center;gap:12px}
.brand-square{width:30px;height:30px;background:var(--yellow)}
.brand-name{font-family:"Lato",sans-serif;font-weight:400;font-size:36px;letter-spacing:1px;color:var(--ink);line-height:1}
.phone-box{left:868px;top:26px;width:52px;height:52px;background:var(--yellow);display:flex;align-items:center;justify-content:center}
.phone-number{left:934px;top:33px;font-family:"Lato",sans-serif;font-size:28px;color:#444}

/* nav */
.main-nav{top:104px;height:54px;background:var(--nav);display:flex;justify-content:center;align-items:center;gap:48px}
.main-nav a{color:var(--white);text-decoration:none;font-size:17px}
.main-nav a.active{color:var(--yellow)}

/* hero */
.hero{top:158px;height:540px;background:linear-gradient(180deg,#f4f6f8 0%,#e8ebee 40%,#c9ced1 70%,#dfe1e2 100%)}
.hero-render{left:0;top:0;width:1200px;height:540px;background:radial-gradient(ellipse at 55% 45%,#6f6e69 0%,#8f8e88 18%,rgba(200,205,200,0) 45%),radial-gradient(ellipse at 88% 30%,#8a9a60 0%,rgba(140,160,100,0) 30%),radial-gradient(ellipse at 15% 60%,#fafafa 0%,rgba(250,250,250,0) 35%)}
.hero-caption{left:347px;top:140px;width:482px;height:255px;background:rgba(40,40,40,.82);display:flex;align-items:center;justify-content:center;text-align:center}
.hero-caption h1{font-family:"Exo 2",sans-serif;font-weight:400;font-size:40px;line-height:46px;color:var(--white);width:400px}
.corner{width:34px;height:34px;border-color:var(--yellow);border-style:solid}
.corner.tl{left:22px;top:16px;border-width:4px 0 0 4px}
.corner.br{right:-18px;bottom:-14px;border-width:0 4px 4px 0}

/* welcome */
.welcome{top:698px;height:434px}
.welcome .title{top:40px}
.welcome p{position:absolute;left:175px;width:850px;text-align:center}
.process .step{width:116px;height:116px;border-radius:50%;background:radial-gradient(circle at 50% 40%,#fffbd0 0%,#fff27a 55%,var(--yellow-deep) 100%);border:6px solid var(--white);box-shadow:0 0 0 2px #f4e050,0 4px 10px rgba(0,0,0,.25);display:flex;align-items:center;justify-content:center;font-size:17px;color:#444}
.process .chev{font-size:36px;color:#555;line-height:1}

/* projects */
.projects{top:1132px;height:468px;background:var(--grey-band)}
.projects .title{top:40px}
.project-strip{left:78px;top:109px;width:1044px;height:291px;display:flex;border:2px solid #ccc}
.project-tile{flex:1;height:100%}
.project-tile.t1{background:linear-gradient(160deg,#e6ecef 0%,#9b9a92 50%,#6e7a55 100%)}
.project-tile.t2{background:linear-gradient(180deg,#cfc8bf 0%,#a9a39a 55%,#76706a 100%);border-top:5px solid var(--yellow)}
.project-tile.t3{background:linear-gradient(180deg,#9fb8d8 0%,#8a8d92 45%,#5e6166 100%)}
.project-tile.t4{background:linear-gradient(180deg,#f5f5f3 0%,#d9d8d4 60%,#bdbcb7 100%)}

/* investment */
.investment{top:1600px;height:296px}
.investment .title{top:45px}
.investment .subtitle{top:100px;left:0;width:1200px;text-align:center;font-family:"Exo 2",sans-serif;font-size:21px;letter-spacing:3px;color:#444}
.investment p{position:absolute;left:170px;width:860px;text-align:center}

/* team */
.team{top:1896px;height:678px;background:var(--grey-band)}
.team .title{top:40px}
.member{width:446px;height:213px}
.member-card{left:30px;top:0;width:416px;height:213px;background:var(--white);box-shadow:2px 6px 10px rgba(0,0,0,.18)}
.member-photo{left:0;top:0;width:198px;height:198px;border:3px solid var(--yellow);background:linear-gradient(180deg,#e9e4da 0%,#b5a999 45%,#3c4654 100%)}
.member-name{left:216px;top:44px;font-size:19px;color:var(--ink)}
.member-bio{left:216px;top:76px;width:210px;font-size:14.5px;line-height:24px}

/* partners */
.partners{top:2574px;height:257px}
.partner-bar{left:78px;top:49px;width:1044px;height:145px;background:#eaeaea;box-shadow:0 10px 12px rgba(0,0,0,.2)}
.partner-label{left:0;top:0;width:210px;height:145px}
.partner-label span{position:absolute;left:0;top:30px;width:170px;text-align:center;font-family:"Exo 2",sans-serif;font-size:30px;line-height:40px;color:var(--white);letter-spacing:1px}
.partner-badge{background:#bdbdbd}

/* news */
.news{top:2831px;height:252px;background:var(--grey-band)}
.news .title{top:40px}
.news-item{top:114px;width:300px;height:100px}
.news-date{left:0;top:0;width:53px;height:73px;background:#d6d6d6;text-align:center;color:#444}
.news-date b{display:block;font-weight:400;font-size:28px;line-height:44px}
.news-date small{display:block;font-size:14px}
.news-text{left:66px;top:2px;width:210px;font-size:14.5px;line-height:23px}
.news-more{left:66px;top:78px;font-size:14.5px;color:#333;text-decoration:underline}

/* contact */
.contact{top:3083px;height:485px}
.contact-info{left:80px;top:0;width:300px;text-align:center}
.contact-info h3{position:absolute;left:0;top:160px;width:300px;font-family:"Exo 2",sans-serif;font-weight:400;font-size:24px;letter-spacing:2px;color:#555}
.contact-info .line{position:absolute;left:0;width:300px;font-size:14.5px;line-height:24px}
.contact-form{left:601px;top:80px;width:519px;height:437px;background:var(--grey-card);box-shadow:0 2px 10px rgba(0,0,0,.3);z-index:2}
.contact-form h2{position:absolute;left:0;top:34px;width:519px;text-align:center;font-family:"Exo 2",sans-serif;font-weight:300;font-size:42px;letter-spacing:3px;color:#444}
.field{left:53px;width:417px;border-bottom:1px solid #888;font-size:14px;color:#555;padding-bottom:4px}
.send{left:53px;top:335px;width:417px;height:40px;background:var(--yellow);border:2px solid #aaa;text-align:center;font-size:18px;line-height:36px;letter-spacing:2px;color:#333}

/* footer */
.site-footer{top:3568px;height:68px;background:var(--footer)}
.site-footer span{position:absolute;left:78px;top:24px;font-size:14.5px;color:var(--yellow)}
</style>
</head>
<body>

<header class="site-header">
  <div class="abs brand"><span class="brand-square"></span><span class="brand-name">Lindwerk</span></div>
  <div class="abs phone-box">
    <svg width="22" height="22" viewBox="0 0 24 24"><path fill="#333" d="M6.6 10.8a15.1 15.1 0 0 0 6.6 6.6l2.2-2.2c.3-.3.7-.4 1-.2 1.1.4 2.3.6 3.6.6.6 0 1 .4 1 1V20c0 .6-.4 1-1 1A17 17 0 0 1 3 4c0-.6.4-1 1-1h3.5c.6 0 1 .4 1 1 0 1.3.2 2.5.6 3.6.1.3 0 .7-.2 1z"/></svg>
  </div>
  <div class="abs phone-number">+43 1 555 0142</div>
</header>

<nav class="main-nav">
  <a class="active" href="#">Home</a><a href="#">Project</a><a href="#">Investment</a><a href="#">Team</a><a href="#">Partner</a><a href="#">News</a><a href="#">Contact</a>
</nav>

<section class="hero">
  <div class="abs hero-render" role="img" aria-label="Architectural rendering of a modern grey residential building with trees and parked cars"></div>
  <div class="abs hero-caption">
    <span class="abs corner tl"></span>
    <h1>We build the best quality at the best price</h1>
    <span class="abs corner br"></span>
  </div>
</section>

<section class="welcome">
  <h2 class="title">WELCOME TO LINDWERK</h2>
  <p style="top:94px">LINDWERK is a group of strong companies that pursue a common goal: the realization of modern, sustainable residential projects for the highest demands in Vienna. The field of work of our development company concentrates on the two core areas of new construction and roof flooring.</p>
  <p style="top:194px">High professional competence, top quality and our many years of experience form a stable foundation, for the realization of living dreams.</p>
  <div class="abs process" style="left:0;top:259px;width:1200px;display:flex;justify-content:center;align-items:center;gap:30px">
    <div class="step">vision</div><span class="chev">»</span>
    <div class="step">conception</div><span class="chev">»</span>
    <div class="step">construction</div><span class="chev">»</span>
    <div class="step">planning</div><span class="chev">»</span>
    <div class="step">sale</div>
  </div>
</section>

<section class="projects">
  <h2 class="title">RECENT PROJECT</h2>
  <div class="abs project-strip">
    <div class="project-tile t1" role="img" aria-label="Rendering of a modern villa exterior"></div>
    <div class="project-tile t2" role="img" aria-label="Rendering of a dining and living interior"></div>
    <div class="project-tile t3" role="img" aria-label="Rendering of an apartment block facade"></div>
    <div class="project-tile t4" role="img" aria-label="Rendering of a bright living room"></div>
  </div>
</section>

<section class="investment">
  <h2 class="title">INVESTMENT</h2>
  <div class="abs subtitle">BUILD A SAFE MONEY</div>
  <p style="top:134px">Invest in the future of living . From an investment of 300,000 euros, you can participate in exclusive attic development and new construction projects of LINDWERK. Benefit from unique success projects with high yield and civic protection .</p>
  <p style="top:200px">Would you like to know more?<br>Just contact us by e-mail at <b>investment@lindwerk.eu</b></p>
</section>

<section class="team">
  <h2 class="title">OUR TEAM</h2>
  <div class="abs member" style="left:128px;top:111px">
    <div class="abs member-card"></div>
    <div class="abs member-photo" role="img" aria-label="Portrait of team member"></div>
    <div class="abs member-name">Markus J. Roth</div>
    <p class="abs member-bio">Lorem Ipsum is simply dummy text of the printing and typesetting industry. Lorem Ipsum has been the industry.</p>
  </div>
  <div class="abs member" style="left:625px;top:111px">
    <div class="abs member-card"></div>
    <div class="abs member-photo" role="img" aria-label="Portrait of team member"></div>
    <div class="abs member-name">Lukas J. Reiter</div>
    <p class="abs member-bio">Lorem Ipsum is simply dummy text of the printing and typesetting industry. Lorem Ipsum has been the industry.</p>
  </div>
  <div class="abs member" style="left:128px;top:392px">
    <div class="abs member-card"></div>
    <div class="abs member-photo" role="img" aria-label="Portrait of team member"></div>
    <div class="abs member-name">Walter R. Stein</div>
    <p class="abs member-bio">Lorem Ipsum is simply dummy text of the printing and typesetting industry. Lorem Ipsum has been the industry.</p>
  </div>
  <div class="abs member" style="left:625px;top:392px">
    <div class="abs member-card"></div>
    <div class="abs member-photo" role="img" aria-label="Portrait of team member"></div>
    <div class="abs member-name">Anna Berger</div>
    <p class="abs member-bio">Lorem Ipsum is simply dummy text of the printing and typesetting industry. Lorem Ipsum has been the industry.</p>
  </div>
</section>

<section class="partners">
  <div class="abs partner-bar">
    <svg class="abs partner-label" viewBox="0 0 210 145" width="210" height="145"><polygon points="0,0 170,0 210,72 170,145 0,145" fill="var(--yellow)"/></svg>
    <div class="abs partner-label"><span>OUR<br>PARTNERS</span></div>
    <div class="abs partner-badge" style="left:278px;top:45px;width:56px;height:56px;border-radius:50%"></div>
    <div class="abs partner-badge" style="left:428px;top:40px;width:200px;height:66px"></div>
    <div class="abs partner-badge" style="left:705px;top:40px;width:210px;height:66px"></div>
    <svg class="abs" style="left:1016px;top:56px" width="16" height="32" viewBox="0 0 16 32"><polyline points="3,3 13,16 3,29" fill="none" stroke="#333" stroke-width="2.5"/></svg>
  </div>
</section>

<section class="news">
  <h2 class="title">LATEST NEWS</h2>
  <div class="abs news-item" style="left:97px">
    <div class="abs news-date"><b>30</b><small>Nov</small></div>
    <p class="abs news-text">There are many variations of passages of Lorem Ipsum available.</p>
    <a class="abs news-more">READ MORE</a>
  </div>
  <div class="abs news-item" style="left:451px">
    <div class="abs news-date"><b>05</b><small>Dec</small></div>
    <p class="abs news-text">There are many variations of passages of Lorem Ipsum available.</p>
    <a class="abs news-more">READ MORE</a>
  </div>
  <div class="abs news-item" style="left:805px">
    <div class="abs news-date"><b>10</b><small>Oct</small></div>
    <p class="abs news-text">There are many variations of passages of Lorem Ipsum available.</p>
    <a class="abs news-more">READ MORE</a>
  </div>
</section>

<section class="contact">
  <div class="abs contact-info">
    <h3>CONTACT INFO</h3>
    <svg class="abs" style="left:139px;top:218px" width="22" height="30" viewBox="0 0 24 32"><path fill="#888" d="M12 0a11 11 0 0 0-11 11c0 8 11 21 11 21s11-13 11-21A11 11 0 0 0 12 0zm0 15a4 4 0 1 1 0-8 4 4 0 0 1 0 8z"/></svg>
    <div class="line" style="top:252px">Lindwerk Group Lindengasse<br>14/2/5 1070 Vienna Austria</div>
    <svg class="abs" style="left:139px;top:310px" width="22" height="22" viewBox="0 0 24 24"><path fill="#888" d="M6.6 10.8a15.1 15.1 0 0 0 6.6 6.6l2.2-2.2c.3-.3.7-.4 1-.2 1.1.4 2.3.6 3.6.6.6 0 1 .4 1 1V20c0 .6-.4 1-1 1A17 17 0 0 1 3 4c0-.6.4-1 1-1h3.5c.6 0 1 .4 1 1 0 1.3.2 2.5.6 3.6.1.3 0 .7-.2 1z"/></svg>
    <div class="line" style="top:338px">+43 1 555 0142</div>
    <svg class="abs" style="left:137px;top:370px" width="26" height="20" viewBox="0 0 26 20"><rect x="1" y="1" width="24" height="18" fill="none" stroke="#888" stroke-width="2"/><polyline points="1,1 13,11 25,1" fill="none" stroke="#888" stroke-width="2"/></svg>
    <div class="line" style="top:396px">office@lindwerk.eu</div>
  </div>
  <form class="abs contact-form">
    <h2>CONTACT US</h2>
    <div class="abs field" style="top:120px">Name</div>
    <div class="abs field" style="top:160px">Email</div>
    <div class="abs field" style="top:201px">Phone</div>
    <div class="abs field" style="top:305px">Message</div>
    <div class="abs send">SEND</div>
  </form>
</section>

<footer class="site-footer"><span>©LINDWERK, 2017 - All Rights Reserved.</span></footer>

</body>
</html>
```